Business Card Design Project

Use our current logo. Clean design.

Industry/Entity Type

Business

Requirements
Must have
• Marisela DUBRANCQ
M. Law
Managing Partner

Alpenvorsa AG
Kornhalmweg 214
CH-3097 Liebefeld

M. +41 79 412 56 27
T. +41 31 928 44 10
F. +41 31 928 44 19

m.dubrancq@alpenvorsa-example.com
www.alpenvorsa-example.com

```html
<!DOCTYPE html>
<html lang="en">
<head>
<meta charset="utf-8">
<title>Alpenvorsa AG – Business Card</title>
<link rel="stylesheet" href="https://fonts.googleapis.com/css2?family=Tenor+Sans&family=Questrial&display=swap">
<style>
  :root {
    --bg: #5a2f1c;
    --card-black: #0d0d0d;
    --card-dark: #2a2a2a;
    --white: #ffffff;
    --ink: #111111;
    --grey: #8a8a8a;
    --grey-light: #b8b8b8;
    --rule: #555555;
  }
  * { margin: 0; padding: 0; box-sizing: border-box; }
  html, body { width: 1200px; height: 1000px; overflow: hidden; }
  body { background: var(--bg); position: relative; font-family: "Questrial", sans-serif; }

  .card { position: absolute; left: 286px; width: 629px; }

  /* Front */
  .card-front {
    top: 104px; height: 343px;
    background: radial-gradient(ellipse at 50% 40%, var(--card-dark) 0%, var(--card-black) 75%);
  }
  .brand-name {
    position: absolute; left: 0; right: 0; top: 218px;
    text-align: center;
    font-family: "Tenor Sans", sans-serif;
    font-size: 50px; letter-spacing: 1px;
    color: var(--white);
  }
  .brand-rule { position: absolute; left: 134px; top: 226px; }
  .brand-web {
    position: absolute; right: 123px; top: 290px;
    font-size: 12px; letter-spacing: 1px; color: var(--white);
  }

  /* Back */
  .card-back {
    top: 540px; height: 358px;
    background: var(--card-black);
  }
  .back-face {
    position: absolute; left: 16px; top: 17px; right: 17px; bottom: 16px;
    background: var(--white);
    overflow: hidden;
  }
  .person { position: absolute; left: 23px; top: 141px; }
  .person-name { font-size: 17px; color: var(--ink); letter-spacing: 0.3px; white-space: nowrap; }
  .person-degree { font-size: 12px; }
  .person-role {
    text-align: right; font-size: 11px; letter-spacing: 1.5px;
    color: var(--grey); margin-top: 1px;
  }
  .divider { position: absolute; left: 297px; top: 122px; width: 1px; height: 78px; background: var(--rule); }
  .contact { position: absolute; left: 326px; top: 127px; font-size: 12px; line-height: 17px; color: var(--ink); text-transform: uppercase; white-space: nowrap; }
  .address { position: absolute; left: 23px; top: 263px; font-size: 13px; line-height: 16px; color: var(--ink); text-transform: uppercase; }
  .corner-name {
    position: absolute; right: 10px; bottom: 12px;
    font-family: "Tenor Sans", sans-serif;
    font-size: 30px; color: var(--grey-light);
  }
</style>
</head>
<body>

<section class="card card-front">
  <svg class="brand-rule" width="360" height="4" viewBox="0 0 360 4" aria-hidden="true">
    <rect x="0" y="1" width="360" height="1.5" fill="#dddddd"/>
  </svg>
  <div class="brand-name">ALPENVORSA</div>
  <div class="brand-web">WWW.ALPENVORSA-EXAMPLE.COM</div>
</section>

<section class="card card-back">
  <div class="back-face">
    <div class="person">
      <div class="person-name">MARISELA DUBRANCQ <span class="person-degree">M. LAW</span></div>
      <div class="person-role">MANAGING PARTNER</div>
    </div>
    <div class="divider"></div>
    <div class="contact">
      <div>M. +41 79 412 56 27</div>
      <div>T. +41 31 928 44 10</div>
      <div>F. +41 31 928 44 19</div>
      <div>m.dubrancq@alpenvorsa-example.com</div>
      <div>www.alpenvorsa-example.com</div>
    </div>
    <div class="address">
      <div>Alpenvorsa AG</div>
      <div>Kornhalmweg 214</div>
      <div>CH-3097 Liebefeld</div>
    </div>
    <div class="corner-name">ALPENVORSA</div>
  </div>
</section>

</body>
</html>
```